Web Design for an Innovative Life Science Marketplace

IMPORTANT:
The software is called CS-Cart. It has capabilities and limitations with design features in the software. There is a certain framework that needs to be followed. It is PHP and Linux. It may require add-ons for your design, so please be specific with what is required. It’s preferred the designer has CS-Cart knowledge/experience.

Key Requirements
1. I’d like the design to include an implemented/recommended CS-Cart theme that is consistent with our branding (see the marketing collateral and logo).
2. I then need the additional design changes to that theme to create the below web pages.
3. All designs should be consistent with our branding. All pictures should either be computer generated (clip art-like) or pictures of happy patients. What is a happy patient? Close up photo of someone healthy, happy, and experiencing/enjoying life. Not someone in a hospital or getting care. Please see examples already on the site.

Please see the attached Web Design details in the word document. That document is important to complete the design.

```html
<!DOCTYPE html>
<html lang="en">
<head>
<meta charset="utf-8">
<title>Materialink — Life Science Marketplace</title>
<link href="https://fonts.googleapis.com/css2?family=Roboto:wght@300;400;500;700;900&family=Roboto+Condensed:wght@400;700&display=swap" rel="stylesheet">
<style>
:root{
  --teal:#17a08f;
  --teal-dark:#0f8071;
  --teal-soft:#5fa9a0;
  --lime:#8cc63f;
  --lime-dark:#74ad2a;
  --ink:#2a2a2a;
  --char:#2d2f31;
  --grey:#6f7275;
  --line:#d5d8da;
  --paper:#ffffff;
  --mist:#f3f5f5;
}
*{box-sizing:border-box;margin:0;padding:0}
html,body{width:1200px;height:3748px;overflow:hidden}
body{font-family:"Roboto",Arial,sans-serif;color:var(--ink);background:var(--paper);font-size:13px;line-height:1.55}
.btn{display:inline-block;font:700 11px "Roboto",sans-serif;letter-spacing:.5px;text-transform:uppercase;color:#fff;padding:9px 20px;border-radius:18px}
.btn-lime{background:var(--lime)}
.btn-teal{background:var(--teal)}
.btn-dark{background:var(--char)}
.ph{display:block}
.cap{font-family:"Roboto Condensed","Roboto",sans-serif;font-weight:700;text-transform:uppercase;letter-spacing:1px}
.cap .big{font-size:1.7em}

/* top bar */
.topbar{height:32px;border-bottom:1px solid var(--line);display:flex;align-items:center;justify-content:space-between;padding:0 150px;font-size:11px;color:var(--grey)}
.topbar .social{display:flex;gap:6px}
.topbar .social span{width:14px;height:14px;background:var(--grey);border-radius:2px}
/* header */
.header{height:120px;display:flex;align-items:center;justify-content:space-between;padding:0 150px}
.brand{display:flex;align-items:center;gap:10px;font:900 24px "Roboto",sans-serif;color:var(--lime)}
.brand .dot{width:30px;height:30px;border-radius:50%;background:var(--teal)}
.header-tools{display:flex;align-items:center;gap:14px}
.cart{display:flex;align-items:center;gap:10px}
.cart .icon{width:44px;height:44px;background:var(--lime);border-radius:4px;display:flex;align-items:center;justify-content:center}
.cart b{display:block;font-size:12px}
.cart small{font-size:11px;color:var(--grey)}
.search{width:180px;height:30px;border:1px solid var(--line);border-radius:15px;display:flex;align-items:center;justify-content:space-between;padding:0 4px 0 12px;font-size:11px;color:#999}
.search i{width:22px;height:22px;border-radius:50%;background:var(--lime)}
/* nav */
.nav{height:28px;background:var(--teal);display:flex;padding:0 150px}
.nav a{color:#fff;font:500 11px "Roboto",sans-serif;text-transform:uppercase;padding:0 18px;line-height:28px;text-decoration:none}
.nav a.on{background:var(--lime-dark)}
/* hero */
.hero{position:relative;height:440px}
.hero .ph{position:absolute;inset:0;background:linear-gradient(100deg,#4d5a4b 0%,#8c9a7f 38%,#c9c1a6 55%,#6f8f5c 80%,#3f5c39 100%)}
.hero-copy{position:absolute;left:150px;top:110px;color:#fff;width:420px}
.hero-copy h1{font:900 58px/1 "Roboto",sans-serif;letter-spacing:2px}
.hero-copy .band{display:inline-block;background:var(--teal);font:700 22px "Roboto Condensed",sans-serif;text-transform:uppercase;padding:4px 14px;margin:8px 0 14px -14px}
.hero-copy p{font-size:12px;line-height:1.5;margin-bottom:22px}
/* section heading */
.sec-head{display:flex;align-items:center;justify-content:center;gap:20px;font-size:30px;color:var(--char)}
.sec-head::before,.sec-head::after{content:"";width:130px;height:2px;background:var(--line)}
.sec-head .big{color:var(--lime)}
.lede{width:880px;margin:24px auto 0;text-align:center;font-size:11px;color:var(--grey);line-height:1.6}
/* who */
.who{height:620px;padding-top:124px}
.who-cards{display:flex;justify-content:center;gap:34px;margin-top:56px}
.who-card{width:270px;background:var(--paper);box-shadow:0 2px 10px rgba(0,0,0,.12);padding:0 26px 30px;position:relative;margin-top:40px}
.who-card .badge{width:70px;height:70px;border-radius:50%;margin:-36px auto 24px;display:flex;align-items:center;justify-content:center}
.who-card h3{font-size:18px;color:var(--char);margin-bottom:10px}
.who-card h3 .big{color:var(--teal)}
.who-card p{font-size:11px;color:var(--grey);margin-bottom:18px}
.who-card .btn{margin-left:60px}
/* about */
.about{display:flex;height:340px;margin-top:40px}
.about-copy{width:730px;background:var(--teal);color:#fff;padding:44px 40px 0 150px}
.about-copy h2{font-size:34px;margin-bottom:16px}
.about-copy p{font-size:11px;line-height:1.6;margin-bottom:12px;opacity:.92}
.about .ph{flex:1;background:linear-gradient(120deg,#6c5a4c,#b79b84 50%,#3e3a36)}
/* product */
.product{height:600px;padding-top:80px}
.products{display:flex;justify-content:center;align-items:flex-end;margin-top:40px}
.prod{width:250px;height:150px;background:var(--teal-soft);color:#fff;text-align:center;padding:18px 20px}
.prod.feature{width:300px;height:220px;background:var(--teal);padding-top:24px}
.prod .ic{width:40px;height:40px;border-radius:50%;background:#fff;margin:0 auto 8px;display:flex;align-items:center;justify-content:center}
.prod h4{font:700 16px "Roboto Condensed",sans-serif;text-transform:uppercase}
.prod.feature h4{font-size:22px}
.prod p{font-size:10px;line-height:1.4;margin:4px 0 10px;opacity:.9}
.prod .btn{font-size:9px;padding:6px 12px;background:rgba(0,0,0,.3)}
.prod.feature .btn{background:var(--lime)}
.all{display:flex;align-items:center;justify-content:center;gap:0;margin-top:44px}
.all::before,.all::after{content:"";width:280px;height:2px;background:var(--line)}
/* marketing */
.marketing{display:flex;height:350px;margin-top:50px}
.marketing .ph{width:470px;background:linear-gradient(110deg,#3d4a52,#8e7f70 45%,#5f6b57)}
.marketing-copy{flex:1;background:var(--lime);color:#fff;padding:40px 150px 0 40px}
.marketing-copy h2{font-size:34px;margin-bottom:16px;color:#fff}
.marketing-copy p{font-size:11px;line-height:1.6;margin-bottom:12px}
.marketing-copy .btns{display:flex;gap:10px;margin-top:14px}
/* promise */
.promise{height:340px;display:flex;justify-content:space-between;align-items:center;padding:0 190px 0 190px}
.promise-copy h2{font-size:34px;color:var(--char)}
.promise-copy h2 .big{color:var(--lime)}
.promise-copy p{font-size:16px;color:var(--grey);width:360px;margin:16px 0 22px;line-height:1.4}
.promise .ph{width:300px;height:230px;background:linear-gradient(135deg,#9fb6c9,#d5c3b0 50%,#6f8a6a)}
/* contact strip */
.contact{height:220px;background:var(--lime);display:flex;justify-content:center;align-items:center;gap:120px;color:#fff}
.contact .item{display:flex;align-items:center;gap:14px}
.contact .circle{width:56px;height:56px;border-radius:50%;border:2px solid #fff;display:flex;align-items:center;justify-content:center}
.contact b{display:block;font-size:16px}
.contact small{font-size:11px;text-transform:uppercase}
/* footer */
.footer{height:480px;background:var(--char);color:#ccc;padding-top:40px}
.footer .connect{text-align:center;font-size:26px;color:#fff}
.footer .connect .big{color:var(--lime)}
.footer .icons{display:flex;justify-content:center;gap:8px;margin-top:12px}
.footer .icons span{width:28px;height:28px;border:1px solid #888;background:#3c3f42}
.cols{display:flex;justify-content:space-between;padding:0 150px;margin-top:54px}
.col{width:260px}
.col h3{font-size:24px;color:#fff;margin-bottom:18px}
.col h3 .big{color:var(--teal)}
.field{height:32px;border-radius:16px;background:#fff;color:#999;font-size:11px;padding:0 14px;line-height:32px;margin-bottom:10px;width:230px}
.col .btn{background:var(--teal)}
.tweet{font-size:11px;line-height:1.5;margin-bottom:14px}
.tweet em{color:var(--lime);font-style:normal}
.col .ph{width:260px;height:150px;background:linear-gradient(135deg,#c9d3c4,#e4e1d6 50%,#b8c7d0)}
.bottom{height:68px;background:var(--teal);display:flex;justify-content:space-between;align-items:center;padding:0 150px;color:#fff;font-size:10px}
.bottom nav a{color:#fff;text-decoration:none;margin-right:22px;text-transform:uppercase}
</style>
</head>
<body>

<div class="topbar">
  <span>Partners · hello@materialink.example · Call us: 555-010-2470</span>
  <div class="social"><span></span><span></span><span></span><span></span></div>
</div>

<header class="header">
  <div class="brand"><span class="dot"></span>MATERIALINK</div>
  <div class="header-tools">
    <div class="cart">
      <div class="icon">
        <svg width="24" height="22" viewBox="0 0 24 22" fill="none" stroke="#fff" stroke-width="2"><path d="M1 2h4l3 12h12l3-9H6"/><circle cx="10" cy="19" r="1.6"/><circle cx="19" cy="19" r="1.6"/></svg>
      </div>
      <div><b>SHOPPING CART</b><small>0 items · $0.00</small></div>
    </div>
    <div class="search">Search <i></i></div>
  </div>
</header>

<nav class="nav">
  <a class="on">Home</a><a>About Us</a><a>Who's Joining</a><a>Our Solutions</a><a>Benefits</a><a>Contact Us</a>
</nav>

<section class="hero">
  <div class="ph" role="img" aria-label="Photo of a smiling woman with long hair enjoying the outdoors by a white fence"></div>
  <div class="hero-copy">
    <h1>JOIN THE</h1>
    <div class="band">Circular Supply Chain</div>
    <p>A modern life science marketplace that links the people who make, study and supply materials, so every resource finds its next good use.</p>
    <span class="btn btn-lime">Learn More About Us</span>
  </div>
</section>

<section class="who">
  <h2 class="sec-head cap"><span><span class="big">W</span>ho Should Join</span></h2>
  <p class="lede">Our marketplace brings together every part of the life science chain. Producers list surplus stock, labs find what they need for the next study, and suppliers reach new buyers. Everyone saves time and cost while fewer good materials are wasted. Join a network that values quality, trust and a shared goal of smarter use of every resource across research and industry.</p>
  <div class="who-cards">
    <article class="who-card">
      <div class="badge" style="background:var(--teal)">
        <svg width="34" height="30" viewBox="0 0 34 30" fill="#fff"><path d="M2 28V12l8 5v-5l8 5v-5l8 5V2h6v26z"/></svg>
      </div>
      <h3 class="cap"><span class="big">M</span>anufacturers</h3>
      <p>List surplus stock and spare parts with ease. Reach verified buyers in labs and clinics, recover value from idle items and keep your production lines lean.</p>
      <span class="btn btn-dark">Learn More</span>
    </article>
    <article class="who-card">
      <div class="badge" style="background:var(--lime)">
        <svg width="30" height="32" viewBox="0 0 30 32" fill="none" stroke="#fff" stroke-width="3"><path d="M11 2v10L3 28h24L19 12V2M8 2h14"/></svg>
      </div>
      <h3 class="cap"><span class="big">R</span>esearchers</h3>
      <p>Find the reagents, tools and equipment you need at fair prices. Compare offers, check sources and get orders to your bench faster than before.</p>
      <span class="btn btn-dark">Learn More</span>
    </article>
    <article class="who-card">
      <div class="badge" style="background:#9aa1a6">
        <svg width="26" height="32" viewBox="0 0 26 32" fill="none" stroke="#fff" stroke-width="2.5"><rect x="2" y="2" width="22" height="28" rx="2"/><path d="M7 10h12M7 16h12M7 22h8"/></svg>
      </div>
      <h3 class="cap"><span class="big">O</span>riginal Suppliers</h3>
      <p>Grow your reach with a trusted channel built for life science. Show your full range, manage offers and build lasting ties with new partners.</p>
      <span class="btn btn-dark">Learn More</span>
    </article>
  </div>
</section>

<section class="about">
  <div class="about-copy">
    <h2 class="cap"><span class="big">A</span>bout Materialink</h2>
    <p>We began with a simple idea: good materials should never sit unused on a shelf. Our team built a marketplace where every item can find its next home in a lab, a plant or a clinic.</p>
    <p>Today we connect makers, researchers and suppliers through one clear platform. Each listing is checked, each partner is vetted and every sale helps close the loop on waste.</p>
    <p>We keep things simple, fair and open, so you can focus on the work that matters most.</p>
    <span class="btn btn-lime">Read More</span>
  </div>
  <div class="ph" role="img" aria-label="Close-up photo of a happy woman holding a cup"></div>
</section>

<section class="product">
  <h2 class="sec-head cap"><span><span class="big">P</span>roduct</span></h2>
  <p class="lede">Browse a growing range of items from trusted sources. From bulk raw materials to spare parts and full equipment, each listing shows clear details, condition and price so you can buy with confidence and get back to your work.</p>
  <div class="products">
    <div class="prod">
      <div class="ic"><svg width="22" height="22" viewBox="0 0 22 22" fill="none" stroke="var(--teal-soft)" stroke-width="2.5"><circle cx="11" cy="11" r="4"/><path d="M11 1v4M11 17v4M1 11h4M17 11h4"/></svg></div>
      <h4>Parts</h4>
      <p>Components and spares for lab and plant systems.</p>
      <span class="btn">View Details</span>
    </div>
    <div class="prod feature">
      <div class="ic"><svg width="22" height="22" viewBox="0 0 22 22" fill="var(--teal)"><path d="M3 20l8-18 8 18z"/></svg></div>
      <h4>Raw Materials</h4>
      <p>Chemicals, reagents and base materials for research and production use.</p>
      <span class="btn">View Details</span>
    </div>
    <div class="prod">
      <div class="ic"><svg width="22" height="22" viewBox="0 0 22 22" fill="none" stroke="var(--teal-soft)" stroke-width="2.5"><circle cx="11" cy="11" r="7"/><circle cx="11" cy="11" r="2"/></svg></div>
      <h4>Equipment</h4>
      <p>Instruments and machines ready for their next lab.</p>
      <span class="btn">View Details</span>
    </div>
  </div>
  <div class="all"><span class="btn btn-dark">View All Products</span></div>
</section>

<section class="marketing">
  <div class="ph" role="img" aria-label="Photo of a group of smiling young friends outdoors"></div>
  <div class="marketing-copy">
    <h2 class="cap"><span class="big">M</span>arketing Materials</h2>
    <p>Learn more about how our marketplace works and what it can do for your team. Our guides cover listing, buying, shipping and the checks we run on every partner.</p>
    <p>Download the brochure to share with colleagues, or read our case studies to see how others cut waste and cost.</p>
    <p>New resources are added each month, so check back often.</p>
    <div class="btns"><span class="btn btn-dark">Read Our White Paper</span><span class="btn btn-teal">Read Our Brochure</span></div>
  </div>
</section>

<section class="promise">
  <div class="promise-copy">
    <h2 class="cap"><span class="big">O</span>ur Promise</h2>
    <p>A greener, more cost efficient, and quality-driven supply chain through a collaborative life sciences marketplace.</p>
    <span class="btn btn-teal">Learn More About Us</span>
  </div>
  <div class="ph" role="img" aria-label="Photo of cheerful friends posing together outdoors"></div>
</section>

<section class="contact">
  <div class="item">
    <div class="circle"><svg width="24" height="24" viewBox="0 0 24 24" fill="#fff"><path d="M6 2l4 5-2 3c1.5 3 3 4.5 6 6l3-2 5 4-3 4C10 21 3 14 2 5z"/></svg></div>
    <div><b>555-010-2470</b><small>Call us today</small></div>
  </div>
  <div class="item">
    <div class="circle"><svg width="26" height="20" viewBox="0 0 26 20" fill="none" stroke="#fff" stroke-width="2"><rect x="1" y="1" width="24" height="18"/><path d="M1 1l12 10L25 1"/></svg></div>
    <div><b>hello@materialink.example</b><small>Drop us a line</small></div>
  </div>
  <div class="item">
    <div class="circle"><svg width="20" height="26" viewBox="0 0 20 26" fill="#fff"><path d="M10 0a9 9 0 00-9 9c0 7 9 17 9 17s9-10 9-17a9 9 0 00-9-9zm0 13a4 4 0 110-8 4 4 0 010 8z"/></svg></div>
    <div><b>48 Harbor Lane, NY</b><small>Company address</small></div>
  </div>
</section>

<footer class="footer">
  <h2 class="connect cap"><span class="big">C</span>onnect With Us</h2>
  <div class="icons"><span></span><span></span><span></span></div>
  <div class="cols">
    <div class="col">
      <h3 class="cap"><span class="big">N</span>ewsletter</h3>
      <div class="field">Enter your email</div>
      <span class="btn">Subscribe</span>
    </div>
    <div class="col">
      <h3 class="cap"><span class="big">U</span>pdates</h3>
      <p class="tweet"><em>@materialink</em> New reagent listings just went live this week, take a look.</p>
      <p class="tweet"><em>@materialink</em> Read how one lab cut supply costs by a third.</p>
      <p class="tweet"><em>@materialink</em> Join our next open webinar on circular sourcing.</p>
    </div>
    <div class="col">
      <h3 class="cap"><span class="big">L</span>ocation</h3>
      <div class="ph" role="img" aria-label="Street map showing the company office location"></div>
    </div>
  </div>
</footer>

<div class="bottom">
  <nav><a>Home</a><a>About Us</a><a>Who's Joining</a><a>Our Solutions</a><a>Benefits</a><a>Contact Us</a></nav>
  <span>© 2024 Materialink · All rights reserved</span>
</div>

</body>
</html>
```